MOLVT Study flyer

I need help designing a flyer for a research study that will include brain imaging in adolescents. The info is in the attached document. The study is called the Marrowby Orchard Lantern Vesper Trail (MOLVT) study. Ideally this would be returned as a document that I can edit in the future as we will have several new recruitment phases (different age groups, etc. I also would love to have a logo designed as part of this project, but I recognize that might be a separate design request.

```html
<!DOCTYPE html>
<html lang="en">
<head>
<meta charset="UTF-8">
<title>MOLVT Study Flyer</title>
<link href="https://fonts.googleapis.com/css2?family=Roboto+Condensed:wght@400;500;700;800&display=swap" rel="stylesheet">
<style>
  :root {
    --page-bg: #eeeae3;
    --paper: #ffffff;
    --teal: #157c82;
    --teal-dark: #116d73;
    --charcoal: #353230;
    --blue-deep: #5a84c7;
    --blue-light: #8eaad6;
    --ink: #1c1c1c;
    --white: #ffffff;
    --navy: #2a3566;
    --art-soft: #c9d9e6;
    --art-mid: #7d97c4;
  }
  * { margin: 0; padding: 0; box-sizing: border-box; }
  html, body { width: 1200px; height: 1200px; overflow: hidden; }
  body {
    background: var(--page-bg);
    font-family: "Roboto Condensed", "Arial Narrow", sans-serif;
    color: var(--ink);
    position: relative;
  }
  .flyer {
    position: absolute;
    left: 189px; top: 30px;
    width: 822px; height: 1140px;
    background: var(--paper);
    overflow: hidden;
  }
  .headline {
    position: absolute; left: 40px; top: 44px;
    font-weight: 700; font-size: 64px; line-height: 66px;
    color: var(--teal); letter-spacing: 0.5px;
  }
  .institution {
    position: absolute; left: 632px; top: 36px;
    display: flex; align-items: center; gap: 10px;
  }
  .institution-mark { width: 30px; height: 30px; background: var(--navy); }
  .institution-name {
    font-size: 20px; font-weight: 500; line-height: 22px; color: var(--navy);
  }
  .question-band {
    position: absolute; left: 0; top: 178px; width: 100%; height: 63px;
    background: var(--charcoal); color: var(--white);
    font-weight: 700; font-size: 32px; line-height: 63px; padding-left: 36px;
  }
  .info-band {
    position: absolute; left: 0; top: 328px; width: 100%; height: 501px;
    background: linear-gradient(90deg, var(--blue-deep) 0%, #6f93cd 55%, var(--blue-light) 100%);
  }
  .art { position: absolute; }
  .art-girl {
    left: 310px; top: 262px; width: 336px; height: 320px;
    border-radius: 48% 48% 12px 12px;
    background: radial-gradient(circle at 50% 45%, var(--art-soft) 0%, #b5c9df 55%, var(--art-mid) 100%);
  }
  .art-brain { left: 188px; top: 274px; width: 110px; height: 86px; border-radius: 45%; background: var(--art-mid); }
  .art-dna-top { left: 656px; top: 266px; width: 92px; height: 102px; border-radius: 14px; background: #5f9aa3; opacity: .85; }
  .art-microscope { left: 676px; top: 352px; width: 110px; height: 170px; border-radius: 14px; background: #4a5a8a; opacity: .8; }
  .art-dna-bottom { left: 696px; top: 814px; width: 106px; height: 116px; border-radius: 14px; background: #5f9aa3; opacity: .85; }
  .intro {
    position: absolute; left: 40px; top: 362px;
    font-size: 25px; line-height: 29.5px; color: var(--white);
  }
  .section-title {
    position: absolute; left: 40px;
    font-weight: 700; font-size: 33px; color: var(--ink); letter-spacing: 0.2px;
  }
  .title-involves { top: 592px; }
  .title-eligible { top: 842px; }
  .bullets { position: absolute; list-style: none; font-size: 24.5px; color: var(--ink); }
  .bullets li { position: relative; padding-left: 26px; }
  .bullets li::before {
    content: ""; position: absolute; left: 4px; top: 12px;
    width: 7px; height: 7px; border-radius: 50%; background: var(--ink);
  }
  .involves-list { left: 70px; top: 637px; line-height: 28.5px; }
  .eligible-list { left: 56px; top: 889px; line-height: 30.5px; }
  .eligible-list li { padding-left: 24px; }
  .eligible-list li::before { top: 13px; }
  .contact-band {
    position: absolute; left: 0; top: 1001px; width: 100%; height: 139px;
    background: var(--teal); color: var(--white); font-weight: 700;
  }
  .contact-call {
    position: absolute; left: 0; top: 14px; width: 100%;
    text-align: center; font-size: 27px; line-height: 33px; letter-spacing: 0.3px;
  }
  .contact-email {
    position: absolute; left: 36px; top: 91px;
    display: flex; align-items: center; gap: 10px; font-size: 28px;
  }
  .contact-pay { position: absolute; right: 40px; top: 91px; font-size: 28px; }
</style>
</head>
<body>
  <main class="flyer">
    <h1 class="headline">ARE YOU THE PARENT<br>OF A CHILD AGE 10-17?</h1>

    <div class="institution">
      <div class="institution-mark"></div>
      <div class="institution-name">Halden Ridge<br>University</div>
    </div>

    <div class="question-band">Do they worry or overthink negative emotions?</div>

    <div class="info-band"></div>

    <div class="art art-brain" role="img" aria-label="Illustration of a brain"></div>
    <div class="art art-girl" role="img" aria-label="Illustration of a worried teenage girl with thought clouds and a parent's hands on her shoulders"></div>
    <div class="art art-dna-top" role="img" aria-label="Illustration of a DNA strand"></div>
    <div class="art art-microscope" role="img" aria-label="Illustration of a microscope"></div>

    <p class="intro">Halden Ridge<br>University researchers<br>are seeking girls age<br>10-17 for a study about<br>brain changes across<br>puberty, anxiety, and<br>depression.</p>

    <h2 class="section-title title-involves">STUDY PARTICIPATION INVOLVES:</h2>
    <ul class="bullets involves-list">
      <li>One one-hour interview (online or in-person) where your child<br>will discuss their thoughts</li>
      <li>Online questionnaires (parent and child)</li>
      <li>One two-hour visit where your child will complete an MRI scan,<br>answer questions about their puberty stage, and have a small<br>hair sample taken to study puberty hormones</li>
    </ul>

    <h2 class="section-title title-eligible">YOUR CHILD MAY BE ELIGIBLE IF THEY:</h2>
    <ul class="bullets eligible-list">
      <li>Are age 10-17</li>
      <li>Tend to worry or overthink negative thoughts</li>
      <li>Have not been diagnosed with psychosis, learning problems, or autism</li>
    </ul>

    <div class="art art-dna-bottom" role="img" aria-label="Illustration of a DNA strand"></div>

    <footer class="contact-band">
      <p class="contact-call">INTERESTED IN PARTICIPATING? WANT MORE INFORMATION?<br>PLEASE CONTACT US!</p>
      <p class="contact-email">
        <svg width="44" height="30" viewBox="0 0 44 30" aria-hidden="true">
          <rect x="2" y="2" width="40" height="26" fill="none" stroke="#ffffff" stroke-width="3"/>
          <polyline points="2,2 22,17 42,2" fill="none" stroke="#ffffff" stroke-width="3"/>
        </svg>
        molvtstudy@haldenridge.edu
      </p>
      <p class="contact-pay">Compensation up to $140</p>
    </footer>
  </main>
</body>
</html>
```